Corwith Lodge website redesign

After 8 years of our current site, we're ready to upgrade our site design. We'd like to generally make it more modern and clean and build it on a CMS like joomla for easier future maintenance.

Our hotel is a family-owned bed and breakfast that competes against much larger hotel chains in Aspen with fancier rooms and larger pricetags. Our hotel is priced moderately and features tasteful, uniquely-design rooms.

We are looking for a website that will showcase the uniqueness of our rooms, the history of the Lodge, and the friendliness of our staff.

Here are some other hotel sites we like:

http://www.brackenfoldhouse.example/

http://www.tollerpeakhaus.example/

http://www.quarrowstay.example/

*********

Scope of Work - I'm looking for a design AND build. The website should be built out in Joomla as part of the final deliverable.
Updates

Current website: http://www.corwithlodge.example/

Explanation of what design + build means:

I am looking for not only the design of the site, but also for the homepage and one subpage to be built out as well. I do NOT need the entire site built - only for those two pages to be built and I will retrofit the remainder of the pages.

Target Market(s)

travellers evaluating hotels in Aspen, Colorado.

Industry/Entity Type

Hotel

Requirements
Must have
• Must, must, must be based on a joomla template. "Rotating" large main image as central position on homepage is a must (see example websites mentioned above).

Nice to have
• We have an existing online reservation system. It would be nice to evaluate placing a "widget" on the homepage that integrates to the online reservation page. Similar to that feature that the Bracken Fold website has at the foot of the main image on their homepage.

```html
<!DOCTYPE html>
<html lang="en">
<head>
<meta charset="utf-8">
<title>Corwith Lodge</title>
<link rel="stylesheet" href="https://fonts.googleapis.com/css2?family=Source+Sans+3:wght@300;400;600&display=swap">
<style>
:root{
  --page-bg:#eeeeec;
  --ink:#2e2e2e;
  --ink-soft:#555;
  --brand:#4a5a66;
  --accent:#8fa3b4;
  --panel:rgba(240,240,238,.9);
  --panel-edge:rgba(255,255,255,.6);
  --nav-top:#ffffff;
  --nav-bottom:#dcdde0;
  --divider:#a9adb3;
  --button:#3b3b3b;
  --field-edge:#9a9a9a;
}
*{box-sizing:border-box;margin:0;padding:0}
html,body{width:1200px;height:720px;overflow:hidden}
body{background:var(--page-bg);font-family:"Source Sans 3",Arial,sans-serif;color:var(--ink);position:relative}
.header{position:absolute;left:0;top:0;width:1200px;height:152px;background:linear-gradient(#f1f1ef,#e9e9e7)}
.brand{position:absolute;left:133px;top:58px;font-size:42px;font-weight:400;color:var(--brand);letter-spacing:.5px}
.booking-call{position:absolute;right:127px;top:64px;font-size:18px;color:var(--ink-soft)}
.booking-call strong{font-size:24px;font-weight:600;color:var(--ink);margin-left:6px}

.hero{position:absolute;left:0;top:152px;width:1200px;height:513px;
  background:
   radial-gradient(ellipse 420px 140px at 600px 200px,#d9d4cd 0,rgba(217,212,205,0) 100%),
   linear-gradient(90deg,#3c3a38 0,#6b6762 10%,#b7b0a6 30%,#cfc9c0 55%,#d6d3cf 78%,#f0eeec 92%,#fafafa 100%);}

.nav{position:absolute;left:110px;top:152px;width:978px;height:52px;background:linear-gradient(var(--nav-top),var(--nav-bottom));border-radius:0 0 3px 3px;display:flex;align-items:center;box-shadow:0 1px 2px rgba(0,0,0,.25)}
.nav-home{width:50px;display:flex;justify-content:center}
.nav a{color:var(--ink);text-decoration:none;font-size:16px;border-left:1px solid var(--divider);line-height:24px;text-align:center;flex:none}
.nav a:nth-of-type(1){width:75px}
.nav a:nth-of-type(2){width:85px}
.nav a:nth-of-type(3){width:121px}
.nav a:nth-of-type(4){width:108px}
.nav a:nth-of-type(5){width:159px}
.nav a:nth-of-type(6){width:156px}
.nav a:nth-of-type(7){width:108px}
.nav a:nth-of-type(8){width:106px}

.welcome{position:absolute;left:110px;top:384px;width:642px;height:261px;background:var(--panel)}
.welcome h1{position:absolute;left:12px;top:16px;font-size:18px;font-weight:400;color:var(--accent)}
.welcome h1::before{content:"";display:inline-block;width:11px;height:11px;background:var(--accent);margin-right:10px}
.welcome h1 span{color:var(--brand)}
.welcome .rule{position:absolute;left:36px;top:43px;width:566px;height:1px;background:#b8b8b8}
.welcome p{position:absolute;left:19px;top:56px;width:612px;font-size:14px;line-height:18px;color:var(--ink)}
.thumbs{position:absolute;left:13px;top:178px;display:flex;gap:2px}
.thumb{width:114px;height:76px}
.thumbs-next{position:absolute;left:598px;top:182px}

.sidebar{position:absolute;left:752px;top:325px;width:340px;height:320px;background:var(--panel);border-left:1px solid var(--panel-edge)}
.search{position:absolute;left:38px;top:12px;display:flex;gap:8px}
.search label{display:block;font-size:11px;text-transform:uppercase;color:var(--ink);margin-bottom:3px}
.field{height:19px;border:1px solid var(--field-edge);background:#fff;font-size:9px;display:flex;align-items:center;justify-content:space-between;padding:0 2px 0 4px}
.book{position:absolute;left:203px;top:73px;width:119px;height:44px;background:var(--button);color:#fff;border-radius:3px;font-size:17px;font-weight:600;display:flex;align-items:center;justify-content:center}
.menu{position:absolute;left:38px;top:75px;list-style:none}
.menu li{height:47px;padding-left:10px}
.menu li.current{border-left:3px solid var(--accent);padding-left:7px;height:28px;margin-bottom:19px}
.menu b{display:block;font-size:20px;font-weight:300;color:#5b6670;line-height:24px}
.menu small{display:block;font-size:9.5px;color:var(--ink-soft);line-height:10px;margin-top:3px}

.footer{position:absolute;left:0;top:681px;width:1200px;text-align:center;font-size:12.5px;color:var(--ink-soft)}
.footer nav a{color:var(--ink-soft);text-decoration:none;padding:0 9px}
.footer nav span{color:#888}
.footer p{margin-top:2px}
</style>
</head>
<body>
<header class="header">
  <div class="brand">Corwith Lodge</div>
  <div class="booking-call">Book online or call <strong>877-555-0148</strong></div>
</header>

<div class="hero" role="img" aria-label="Rotating photo of a modern guest room with a double bed, bedside lamps and sheer curtains"></div>

<nav class="nav">
  <span class="nav-home"><svg width="28" height="24" viewBox="0 0 28 24"><path d="M2 12 14 2l12 10" fill="none" stroke="#111" stroke-width="3"/><path d="M6 11v12h6v-7h4v7h6V11L14 4z" fill="#111"/><rect x="20" y="3" width="3" height="6" fill="#111"/></svg></span>
  <a href="#">About</a><a href="#">Rooms</a><a href="#">Reservations</a><a href="#">Amenities</a><a href="#">Aspen information</a><a href="#">Manager's Journal</a><a href="#">Webcams</a><a href="#">Contact Us</a>
</nav>

<section class="welcome">
  <h1>Welcome to <span>Corwith Lodge</span></h1>
  <div class="rule"></div>
  <p>Located in the heart of downtown Aspen, the newly renovated Corwith Lodge possesses all the charms of a vintage European Ski Lodge, while offering all of the modern conveniences one would expect with a stay in Aspen.A stay at our lodge includes free continental breakfast in our dining room, daily maid service, free wireless internet access, and a fully-equipped conference facility. Guests are also invited to relax in one of our two outdoor hot tubs or in our lounge, where a 42-inch plasma TV and fireplace make for a pleasant area to unwind.</p>
  <div class="thumbs">
    <div class="thumb" role="img" aria-label="Lounge with teal sofa" style="background:linear-gradient(#e8e6df,#3a9a8c 70%,#7a6a5a)"></div>
    <div class="thumb" role="img" aria-label="Bright bedroom" style="background:linear-gradient(#eeeae4,#c9bfb1 70%,#8a7a68)"></div>
    <div class="thumb" role="img" aria-label="Bedroom with garden view" style="background:linear-gradient(90deg,#7f9a7a,#d8d2c8 50%,#a08060)"></div>
    <div class="thumb" role="img" aria-label="Bed with colourful cushions" style="background:linear-gradient(#5a3a2a,#c04030 50%,#e8c040 75%,#f0ece8)"></div>
    <div class="thumb" role="img" aria-label="Wood-panelled guest room" style="background:linear-gradient(90deg,#8a5a30,#c89a68 50%,#e8e2da)"></div>
  </div>
  <svg class="thumbs-next" width="8" height="28" viewBox="0 0 8 28"><path d="M0 0l8 6-8 6z M8 16l-8 6 8 6z" fill="#7d97ac"/></svg>
</section>

<aside class="sidebar">
  <div class="search">
    <div><label>Arrival</label><div class="field" style="width:80px">CHECK IN <svg width="14" height="14" viewBox="0 0 14 14" fill="#aaa"><rect x="0" y="0" width="4" height="4"/><rect x="5" y="0" width="4" height="4"/><rect x="10" y="0" width="4" height="4"/><rect x="0" y="5" width="4" height="4"/><rect x="5" y="5" width="4" height="4"/><rect x="10" y="5" width="4" height="4"/><rect x="0" y="10" width="4" height="4"/><rect x="5" y="10" width="4" height="4"/><rect x="10" y="10" width="4" height="4"/></svg></div></div>
    <div><label>Departure</label><div class="field" style="width:79px">CHECK OUT <svg width="14" height="14" viewBox="0 0 14 14" fill="#aaa"><rect x="0" y="0" width="4" height="4"/><rect x="5" y="0" width="4" height="4"/><rect x="10" y="0" width="4" height="4"/><rect x="0" y="5" width="4" height="4"/><rect x="5" y="5" width="4" height="4"/><rect x="10" y="5" width="4" height="4"/><rect x="0" y="10" width="4" height="4"/><rect x="5" y="10" width="4" height="4"/><rect x="10" y="10" width="4" height="4"/></svg></div></div>
    <div><label>Adults</label><div class="field" style="width:52px">-- <svg width="14" height="12" viewBox="0 0 14 12"><rect x=".5" y=".5" width="13" height="11" fill="#eee" stroke="#777"/><path d="M3 4h8l-4 5z" fill="#222"/></svg></div></div>
    <div><label>Children</label><div class="field" style="width:52px">-- <svg width="14" height="12" viewBox="0 0 14 12"><rect x=".5" y=".5" width="13" height="11" fill="#eee" stroke="#777"/><path d="M3 4h8l-4 5z" fill="#222"/></svg></div></div>
  </div>
  <ul class="menu">
    <li class="current"><b>HOME</b><small>welcome to home</small></li>
    <li><b>RESORT</b><small>book resort</small></li>
    <li><b>BREAKFAST</b><small>order to breakfast</small></li>
    <li><b>PHOTOS</b><small>view our photos</small></li>
    <li><b>CONTACT</b><small>contact us</small></li>
  </ul>
  <div class="book">BOOK NOW</div>
</aside>

<footer class="footer">
  <nav><a href="#">Home</a><span>|</span><a href="#">About</a><span>|</span><a href="#">Rooms</a><span>|</span><a href="#">Amenties</a><span>|</span><a href="#">Contact Us</a></nav>
  <p>©2012 Corwith Lodge, Inc</p>
</footer>
</body>
</html>
```